New Dental Office Needs an Attractive and user friendly Website Designed

I need a website for a new dental office. The Name is Maplecrest Dentistry. I would like a Modern design with a user friendly interface and usability.
I would like a landing page, a page that lists the services we offer: Cosmetic Dentistry, Implants, Dental Hygiene, Emergency Services, Restorations, Dentures
Target Market(s)
Mid to upper class
Industry/Entity Type
Dentistry
Coding
Coded - Design and coding required
Number of Pages Required
1 page
Requirements
Must have
- Landing page that has a scheduling option, Procedures, operating hours, and contact us info
Nice to have
- Appealing design, Soft comforting colors. Easy to navigate page, Modern and professional.

```html
<!DOCTYPE html>
<html lang="en">
<head>
<meta charset="utf-8">
<title>Maplecrest Dentistry</title>
<link rel="stylesheet" href="https://fonts.googleapis.com/css2?family=Libre+Baskerville:wght@400;700&family=Montserrat:ital,wght@0,400;0,500;0,600;0,700;1,400&display=swap">
<style>
:root{
  --teal:#2cc6dc;
  --teal-soft:#bdeef5;
  --navy:#1b2a52;
  --ink:#111;
  --grey:#777;
  --white:#fff;
  --black:#000;
}
*{margin:0;padding:0;box-sizing:border-box}
html,body{width:1200px;height:4294px;overflow:hidden;background:var(--white)}
body{position:relative;font-family:"Montserrat",sans-serif;color:var(--ink)}
.abs{position:absolute}
.serif{font-family:"Libre Baskerville",serif}

/* header */
.brand{left:40px;top:38px;font-family:"Libre Baskerville",serif;font-size:30px;color:var(--teal);font-weight:400;white-space:nowrap}
.topbar{left:440px;top:0;width:760px;height:45px;background:var(--teal);border-radius:0 0 0 24px;color:var(--white);font-size:16px;font-weight:500}
.topbar span{position:absolute;top:13px;display:flex;align-items:center;gap:10px}
.nav{top:82px;font-size:19px;font-weight:500;color:#222}

/* hero */
.hero{left:0;top:138px;width:1200px;height:690px;overflow:hidden}
.hero-photo{position:absolute;inset:0;background:linear-gradient(100deg,#16214a 0%,#1f3160 45%,#3a6a72 75%,#5f8f86 100%)}
.hero svg{position:absolute;left:0;top:0}
.hero-kicker{left:86px;top:160px;font-size:34px;color:var(--teal);font-weight:500;letter-spacing:1px}
.hero-title{left:78px;top:205px;font-size:66px;line-height:76px;color:var(--white);font-weight:400}
.btn{display:flex;align-items:center;justify-content:center;border-radius:30px;font-weight:500;text-transform:uppercase}
.hero-btn1{left:78px;top:377px;width:190px;height:52px;background:var(--teal);color:var(--white);font-size:19px}
.hero-btn2{left:285px;top:377px;width:192px;height:52px;border:2px solid var(--white);color:var(--white);font-size:19px}

/* section titles */
.sec-title{left:0;width:1200px;text-align:center;font-size:40px;font-weight:400}
.rule{left:538px;width:124px;height:3px;background:var(--teal)}

/* service cards */
.card{width:268px;height:378px;background:var(--white);border-radius:12px;box-shadow:0 6px 22px rgba(0,0,0,.08);overflow:hidden}
.card .img{position:absolute;left:0;top:0;width:268px;height:163px}
.card .icon{position:absolute;left:96px;top:125px;width:76px;height:76px;border-radius:50%;background:var(--white);border:3px solid var(--teal);display:flex;align-items:center;justify-content:center}
.card h3{position:absolute;top:222px;width:100%;text-align:center;font-size:21px;font-weight:600;color:#222}
.card p{position:absolute;left:24px;right:24px;top:255px;text-align:center;font-size:10.5px;line-height:14px;color:var(--grey)}
.card .more{position:absolute;left:58px;top:333px;width:152px;height:35px;background:var(--teal);color:var(--white);font-size:12px;font-weight:600}
.chev{width:22px;height:22px}
.more-services{left:0;top:1488px;width:1200px;display:flex;justify-content:center;gap:14px}
.service-pill{height:34px;padding:0 22px;border:2px solid var(--teal);border-radius:20px;color:#222;font-size:13px;font-weight:600;display:flex;align-items:center}

/* about */
.about{left:0;top:1563px;width:1200px;height:534px;background:var(--teal)}
.about-photo{position:absolute;left:0;top:0;width:540px;height:534px;background:linear-gradient(135deg,#dfe7ee 0%,#c7d6e3 45%,#8fa6c6 75%,#3e5fa8 100%);border-radius:0 320px 320px 0/0 267px 267px 0}
.about h2{position:absolute;left:600px;top:138px;font-size:40px;color:var(--white);font-weight:400}
.about p{position:absolute;left:602px;top:205px;width:440px;font-size:12.4px;line-height:15.6px;color:var(--white)}
.about .more{position:absolute;left:597px;top:419px;width:151px;height:36px;border:2px solid var(--white);color:var(--white);font-size:13px}

/* steps */
.step-num{width:84px;height:84px;border-radius:50%;background:var(--teal);color:var(--white);font-size:50px;font-weight:700;display:flex;align-items:center;justify-content:center}
.step-label{font-size:21px;font-weight:700}
.step-text{width:230px;font-size:10.5px;line-height:14px;color:var(--grey)}

/* testimonials */
.review{width:273px;height:330px;background:var(--white);border-radius:16px;box-shadow:0 6px 24px rgba(0,0,0,.07)}
.review .quote{position:absolute;left:16px;top:12px}
.review .avatar{position:absolute;left:94px;top:25px;width:84px;height:84px;border-radius:50%;background:radial-gradient(circle at 50% 40%,#b9a592,#5a4d47)}
.review h4{position:absolute;top:140px;width:100%;text-align:center;font-family:"Libre Baskerville",serif;font-size:13px;font-weight:700}
.review p{position:absolute;left:30px;right:30px;top:166px;text-align:center;font-style:italic;font-size:13px;line-height:16px;color:var(--grey)}
.review .stars{position:absolute;top:282px;width:100%;text-align:center;color:var(--teal);font-size:20px;letter-spacing:2px}

/* schedule */
.schedule{left:0;top:3233px;width:1200px;height:1061px;background:linear-gradient(180deg,#2cc6dc 0%,#3fcde0 100%)}
.schedule h2{position:absolute;top:100px;width:100%;text-align:center;font-size:38px;color:var(--white);font-weight:400}
.field{position:absolute;background:var(--teal-soft);color:#555;font-size:17px;padding:0 30px;display:flex;align-items:center}
.submit{left:440px;top:454px;width:382px;height:58px;border:2px solid var(--white);color:var(--white);font-size:18px}

/* footer */
.footer{left:0;top:3760px;width:1200px;height:534px}
.footer svg{position:absolute;left:0;top:0}
.f-brand{left:130px;top:248px;font-family:"Libre Baskerville",serif;font-size:24px;color:var(--white);white-space:nowrap}
.social{width:22px;height:22px;border-radius:50%;background:var(--teal)}
.f-head{font-family:"Libre Baskerville",serif;font-size:13px;color:var(--white)}
.f-link{font-size:12px;color:var(--white);font-weight:500}
.f-info{left:610px;font-size:12px;color:var(--white);line-height:17px}
.f-email{left:858px;top:280px;width:167px;height:27px;border-radius:14px;background:#333;color:#999;font-size:10px;display:flex;align-items:center;justify-content:center}
.f-sub{left:858px;top:318px;width:165px;height:28px;border-radius:14px;background:var(--teal);color:var(--white);font-size:11px;font-weight:600;display:flex;align-items:center;justify-content:center}
.f-hours{left:862px;top:372px;font-size:11px;line-height:16px;color:var(--white)}
.f-hours b{display:block;font-family:"Libre Baskerville",serif;font-weight:400;font-size:12px;margin-bottom:4px}
.copy{left:0;top:455px;width:1200px;text-align:center;font-size:9px;color:var(--white)}
</style>
</head>
<body>

<!-- header -->
<div class="abs brand">Maplecrest Dentistry</div>
<div class="abs topbar">
  <span style="left:122px">
    <svg width="20" height="16" viewBox="0 0 20 16"><rect x="1" y="4" width="18" height="11" fill="#fff"/><path d="M1 5 L10 11 L19 5" stroke="#2cc6dc" stroke-width="1.6" fill="none"/><path d="M4 4 L10 0.5 L16 4" fill="#fff"/></svg>
    SCHEDULE AN APPOINTMENT</span>
  <span style="left:500px;font-size:18px">
    <svg width="20" height="20" viewBox="0 0 24 24"><path fill="#fff" d="M6.6 10.8a15.2 15.2 0 0 0 6.6 6.6l2.2-2.2a1 1 0 0 1 1-.25 11.4 11.4 0 0 0 3.6.57 1 1 0 0 1 1 1V20a1 1 0 0 1-1 1A17 17 0 0 1 3 4a1 1 0 0 1 1-1h3.5a1 1 0 0 1 1 1c0 1.25.2 2.45.57 3.6a1 1 0 0 1-.25 1z"/></svg>
    (123) 555 0148</span>
</div>
<div class="abs nav" style="left:475px">HOME</div>
<div class="abs nav" style="left:597px">ABOUT</div>
<div class="abs nav" style="left:737px">SERVICES</div>
<div class="abs nav" style="left:900px">DOCTORS</div>
<div class="abs nav" style="left:1064px">CONTACT</div>

<!-- hero -->
<section class="abs hero">
  <div class="hero-photo" role="img" aria-label="Photo of a dentist in mask and scrubs treating a smiling patient in the chair"></div>
  <svg width="1200" height="690" viewBox="0 0 1200 690">
    <path d="M0 460 Q600 880 1200 470 L1200 690 L0 690Z" fill="#2cc6dc"/>
    <path d="M0 482 Q600 920 1200 488 L1200 690 L0 690Z" fill="#fff"/>
  </svg>
  <div class="abs hero-kicker">WELCOME TO</div>
  <h1 class="abs hero-title serif">MAPLECREST<br>DENTISTRY</h1>
  <div class="abs btn hero-btn1">Appointment</div>
  <div class="abs btn hero-btn2">Our Services</div>
</section>

<!-- what we do -->
<h2 class="abs sec-title serif" style="top:930px">WHAT WE DO</h2>
<div class="abs rule" style="top:983px"></div>

<svg class="abs chev" style="left:41px;top:1218px" viewBox="0 0 22 22"><path d="M15 2 L6 11 L15 20" stroke="#222" stroke-width="2.4" fill="none"/></svg>
<svg class="abs chev" style="left:1137px;top:1236px" viewBox="0 0 22 22"><path d="M7 2 L16 11 L7 20" stroke="#222" stroke-width="2.4" fill="none"/></svg>

<article class="abs card" style="left:150px;top:1075px">
  <div class="img" role="img" aria-label="Photo of a patient with open mouth during a cosmetic dental treatment" style="background:linear-gradient(135deg,#e9eef3,#b8cde0 60%,#7fa3c4)"></div>
  <div class="icon"><svg width="42" height="42" viewBox="0 0 42 42" fill="none" stroke="#2cc6dc" stroke-width="2"><path d="M12 8c-5 0-7 5-6 10 1 4 3 6 3 11 0 4 2 7 4 7s3-4 4-8c1-3 2-4 4-4s3 1 4 4c1 4 2 8 4 8s4-3 4-7c0-5 2-7 3-11 1-5-1-10-6-10-4 0-5 2-9 2s-5-2-9-2z"/><circle cx="29" cy="18" r="5"/><path d="M29 15v6M26 18h6"/></svg></div>
  <h3>Cosmetic Dentistry</h3>
  <p>Gentle treatments that brighten and reshape your smile, planned around your goals so every visit feels calm, simple and comfortable from start to finish.</p>
  <div class="btn more">Read More</div>
</article>

<article class="abs card" style="left:477px;top:1075px">
  <div class="img" role="img" aria-label="Photo of a dentist consulting with a smiling patient about implants" style="background:linear-gradient(135deg,#f0f2f4,#c9d7e2 55%,#8fb6cf)"></div>
  <div class="icon"><svg width="42" height="42" viewBox="0 0 42 42" fill="none" stroke="#2cc6dc" stroke-width="2"><path d="M11 8c3-2 6 0 10 0s7-2 10 0c2 2 1 6-1 8H12c-2-2-3-6-1-8z"/><path d="M14 19h14M15 23h12M16 27h10M17 31h8M19 35h4"/></svg></div>
  <h3>Dental Implants</h3>
  <p>Lasting replacements for missing teeth, placed with care by our team to restore your bite and your confidence.</p>
  <div class="btn more">Read More</div>
</article>

<article class="abs card" style="left:803px;top:1075px">
  <div class="img" role="img" aria-label="Photo of a dental team performing a hygiene cleaning in a bright clinic" style="background:linear-gradient(135deg,#e6ecf0,#c3d1dc 55%,#9eb4c4)"></div>
  <div class="icon"><svg width="42" height="42" viewBox="0 0 42 42" fill="none" stroke="#2cc6dc" stroke-width="2"><path d="M12 14c-4 0-6 4-5 8 1 3 3 5 3 9 0 3 1 5 3 5s2-3 3-6c1-2 2-3 5-3s4 1 5 3c1 3 1 6 3 6s3-2 3-5c0-4 2-6 3-9 1-4-1-8-5-8-3 0-5 2-9 2s-6-2-9-2z"/><path d="M10 8h22M14 5v3M18 5v3M22 5v3M26 5v3"/></svg></div>
  <h3 style="top:225px">Dental Hygiene</h3>
  <p style="top:258px">Regular cleanings and check-ups keep gums healthy, and our hygienists explain simple habits you can add at home.</p>
  <div class="btn more">Read More</div>
</article>

<div class="abs more-services">
  <div class="service-pill">Emergency Services</div>
  <div class="service-pill">Restorations</div>
  <div class="service-pill">Dentures</div>
</div>

<!-- about -->
<section class="abs about">
  <div class="about-photo" role="img" aria-label="Photo of a dentist and assistant in white coats treating a patient"></div>
  <h2 class="serif">ABOUT US</h2>
  <p>Lorem ipsum dolor sit amet, consectetuer adipiscing elit, sed diam nonummy nibh euismod tincidunt ut laoreet dolore magna aliquam erat volutpat. Ut wisi enim ad minim veniam, quis nostrud exerci tation ullamcorper suscipit lobortis nisl ut aliquip ex ea commodo consequat. Duis autem vel eum iriure dolor in hendrerit in vulputate velit esse molestie consequat, vel illum dolore eu feugiat nulla facilisis at vero eros et accumsan et iusto odio dignissim qui blandit praesent luptatum zzril delenit augue duis dolore te feugait nulla facilisi.<br>Lorem ipsum dolor sit amet, cons ectetuer adipiscing elit, sed diam nonummy nibh euismod tincidunt ut laoreet dolore magna aliquam erat volutpat. Ut wisi enim ad minim veniam, quis nostrud exerci</p>
  <div class="btn more">Read More</div>
</section>

<!-- how it works -->
<h2 class="abs sec-title serif" style="top:2190px">HOW IT WORKS</h2>
<div class="abs rule" style="top:2248px;left:514px"></div>

<svg class="abs" style="left:0;top:2355px" width="1200" height="4"><path d="M222 2H456M544 2H792" stroke="#2cc6dc" stroke-width="1.6" stroke-dasharray="7 6"/></svg>

<div class="abs step-num" style="left:136px;top:2315px">1</div>
<div class="abs step-num" style="left:458px;top:2315px">2</div>
<div class="abs step-num" style="left:794px;top:2315px">3</div>

<div class="abs step-label" style="left:137px;top:2418px">STEP 1</div>
<div class="abs step-label" style="left:460px;top:2418px">STEP 2</div>
<div class="abs step-label" style="left:795px;top:2418px">STEP 3</div>

<p class="abs step-text" style="left:135px;top:2457px">Lorem ipsum dolor sit amet, consectetuer adipiscing elit, sed diam nonummy nibh euismod tincidunt ut laoreet dolore magna</p>
<p class="abs step-text" style="left:460px;top:2457px">Lorem ipsum dolor sit amet, consectetuer adipiscing elit, sed diam nonummy nibh euismod tincidunt ut laoreet dolore magna</p>
<p class="abs step-text" style="left:802px;top:2462px">Lorem ipsum dolor sit amet, consectetuer adipiscing elit, sed diam nonummy nibh euismod tincidunt ut laoreet dolore magna</p>

<!-- testimonials -->
<h2 class="abs sec-title serif" style="top:2655px">WHAT CLIENT SAY’S</h2>
<div class="abs rule" style="top:2720px;left:518px"></div>

<svg class="abs chev" style="left:54px;top:2908px" viewBox="0 0 22 22"><path d="M15 2 L6 11 L15 20" stroke="#222" stroke-width="2.4" fill="none"/></svg>
<svg class="abs chev" style="left:1129px;top:2926px" viewBox="0 0 22 22"><path d="M7 2 L16 11 L7 20" stroke="#222" stroke-width="2.4" fill="none"/></svg>

<article class="abs review" style="left:147px;top:2768px">
  <svg class="quote" width="32" height="26" viewBox="0 0 32 26"><path fill="#2cc6dc" d="M0 0h13v13L7 26H2l4-13H0zM18 0h13v13l-6 13h-5l4-13h-6z"/></svg>
  <div class="avatar" role="img" aria-label="Portrait photo of the client"></div>
  <h4>OWEN MARSH</h4>
  <p>Lorem ipsum dolor sit amet, consectetuer adipiscing elit, sed diam nonummy nibh euismod tincidunt ut laoreet dolore magna aliquam</p>
  <div class="stars">★★★★★</div>
</article>
<article class="abs review" style="left:467px;top:2768px">
  <svg class="quote" width="32" height="26" viewBox="0 0 32 26"><path fill="#2cc6dc" d="M0 0h13v13L7 26H2l4-13H0zM18 0h13v13l-6 13h-5l4-13h-6z"/></svg>
  <div class="avatar" role="img" aria-label="Portrait photo of the client" style="background:radial-gradient(circle at 50% 40%,#8a6a55,#2d2320)"></div>
  <h4>DK PALMER</h4>
  <p>Lorem ipsum dolor sit amet, consectetuer adipiscing elit, sed diam nonummy nibh euismod tincidunt ut laoreet dolore magna aliquam</p>
  <div class="stars">★★★★★</div>
</article>
<article class="abs review" style="left:787px;top:2768px">
  <svg class="quote" width="32" height="26" viewBox="0 0 32 26"><path fill="#2cc6dc" d="M0 0h13v13L7 26H2l4-13H0zM18 0h13v13l-6 13h-5l4-13h-6z"/></svg>
  <div class="avatar" role="img" aria-label="Portrait photo of the client" style="background:radial-gradient(circle at 50% 40%,#9a6a60,#3a2226)"></div>
  <h4>RINA L CASTELL</h4>
  <p>Lorem ipsum dolor sit amet, consectetuer adipiscing elit, sed diam nonummy nibh euismod tincidunt ut laoreet dolore magna aliquam</p>
  <div class="stars">★★★★★</div>
</article>

<!-- schedule -->
<section class="abs schedule">
  <h2 class="serif">SCHEDULE AN APPOINTMENT</h2>
  <div class="abs rule" style="top:158px;left:526px;background:#fff;width:140px"></div>
  <div class="field" style="left:108px;top:207px;width:313px;height:49px">FULL NAME</div>
  <div class="field" style="left:443px;top:207px;width:313px;height:49px">EMAIL ADDRESS</div>
  <div class="field" style="left:778px;top:207px;width:313px;height:49px">PHONE NUMBER</div>
  <div class="field" style="left:108px;top:290px;width:983px;height:133px;align-items:flex-start;padding-top:28px">ADDITIONAL MESSAGE</div>
  <div class="abs btn submit">Get an Appointment</div>
</section>

<!-- footer -->
<footer class="abs footer">
  <svg width="1200" height="534" viewBox="0 0 1200 534">
    <path d="M0 222 Q600 -200 1200 222 L1200 534 L0 534Z" fill="#fff"/>
    <path d="M0 240 Q600 -180 1200 240 L1200 534 L0 534Z" fill="#000"/>
  </svg>
  <div class="abs f-brand">Maplecrest Dentistry</div>
  <div class="abs social" style="left:152px;top:322px"></div>
  <div class="abs social" style="left:191px;top:322px"></div>
  <div class="abs social" style="left:230px;top:322px"></div>

  <div class="abs f-head" style="left:390px;top:218px">QUICK LINKS</div>
  <div class="abs f-link" style="left:402px;top:268px">HOME</div>
  <div class="abs f-link" style="left:402px;top:299px">SERVICES</div>
  <div class="abs f-link" style="left:402px;top:330px">PRICING</div>
  <div class="abs f-link" style="left:402px;top:360px">ABOUT</div>
  <div class="abs f-link" style="left:402px;top:391px">CONTACT</div>

  <div class="abs f-head" style="left:567px;top:218px">CONTACT NFO</div>
  <svg class="abs" style="left:567px;top:265px" width="18" height="18" viewBox="0 0 24 24"><path fill="#2cc6dc" d="M6.6 10.8a15.2 15.2 0 0 0 6.6 6.6l2.2-2.2a1 1 0 0 1 1-.25 11.4 11.4 0 0 0 3.6.57 1 1 0 0 1 1 1V20a1 1 0 0 1-1 1A17 17 0 0 1 3 4a1 1 0 0 1 1-1h3.5a1 1 0 0 1 1 1c0 1.25.2 2.45.57 3.6a1 1 0 0 1-.25 1z"/></svg>
  <div class="abs f-info" style="top:266px">(123) 555 0192</div>
  <svg class="abs" style="left:567px;top:308px" width="18" height="15" viewBox="0 0 20 16"><rect x="1" y="4" width="18" height="11" fill="#2cc6dc"/><path d="M1 5 L10 11 L19 5" stroke="#000" stroke-width="1.6" fill="none"/><path d="M4 4 L10 0.5 L16 4" fill="#2cc6dc"/></svg>
  <div class="abs f-info" style="top:308px">hello@maplecrestdental.example</div>
  <svg class="abs" style="left:568px;top:350px" width="16" height="20" viewBox="0 0 16 20"><path fill="#2cc6dc" d="M8 0a7 7 0 0 0-7 7c0 5 7 13 7 13s7-8 7-13a7 7 0 0 0-7-7zm0 10a3 3 0 1 1 0-6 3 3 0 0 1 0 6z"/></svg>
  <div class="abs f-info" style="top:351px">Lindenvale Centre,<br>218 Harbour Lane,<br>Eastbrook 5521</div>

  <div class="abs f-head" style="left:862px;top:218px">STAY UP-TO-DATE</div>
  <div class="abs f-email">EMAIL ADDRESS</div>
  <div class="abs f-sub">SUBSCRIBE NOW</div>
  <div class="abs f-hours"><b>OPENING HOURS</b>Mon – Fri: 8:00 am – 6:00 pm<br>Sat: 9:00 am – 2:00 pm<br>Sun: Closed</div>

  <div class="abs copy">© 2025 DENTAL WEBSITE. ALL RIGHTS RESERVED.</div>
</footer>

</body>
</html>
```